Thornfield Marsh, LLC Website

We are a small law firm in need of a website that contains the following:
1. Attractive main page
2. About us/attorney info for three people: Leonard Thornfield (attorney), Brent Marsh (attorney), and Melinda Carrow (legal assistant). We have bio's ready to submit.
3. Blog/video page. We'd like to post blogs and videos to help drive traffic
4. Multidistrict Litigation and Class Actions page, where we post information regarding active MDLs and Class actions that we are doing intake on.
Updates

Can you also please use the color "gold" in the design and logo? Thanks.

Industry/Entity Type

Legal

Coding

Coded - Design and coding required

Number of Pages Required

1 page

Colors
0054AA
0677BA
7BADD7
CADEEF
E8F1F8

Requirements
Must have
• 1. Attractive main page 2. About us/attorney info for three people: Leonard Thornfield (attorney), Brent Marsh (attorney), and Melinda Carrow (legal assistant). We have bio's ready to submit. 3. Blog/video page. We'd like to post blogs and videos to help drive traffic 4. Multidistrict Litigation and Class Actions page, where we post information regarding active MDLs and Class actions that we are doing intake on.

```html
<!DOCTYPE html>
<html lang="en">
<head>
<meta charset="utf-8">
<title>Thornfield Marsh, LLC</title>
<link href="https://fonts.googleapis.com/css2?family=Montserrat:wght@400;500;600;700;800&display=swap" rel="stylesheet">
<style>
:root{
  --navy:#262a74;
  --navy-deep:#1b1f5e;
  --blue:#3a9fe0;
  --blue-dark:#0054aa;
  --blue-mid:#0677ba;
  --gold:#f5a41f;
  --ink:#151515;
  --text:#333;
  --muted:#555;
  --grey-card:#e9e9ea;
  --white:#fff;
}
*{box-sizing:border-box;margin:0;padding:0}
html,body{width:1200px;height:4605px;overflow:hidden}
body{font-family:"Montserrat",sans-serif;color:var(--text);background:var(--white);position:relative}
section,header,footer{position:absolute;left:0;width:1200px;overflow:hidden}
.btn{position:absolute;background:var(--gold);color:var(--white);font-weight:700;font-size:11px;display:flex;align-items:center;justify-content:center;gap:6px}
.brand{position:absolute;display:flex;align-items:center;gap:8px;border:2px solid var(--navy);background:var(--white);padding:0 10px}
.brand .mark{width:14px;height:14px;background:var(--blue)}
.brand span{font-weight:700;color:var(--navy);font-size:13px;white-space:nowrap}
.sec-title{position:absolute;left:0;width:1200px;display:flex;justify-content:center;align-items:center;gap:8px;color:var(--navy);font-weight:700;font-size:29px}
.sec-title::before,.sec-title::after{content:"";width:70px;height:2px;background:var(--navy)}
.photo{position:absolute}

/* header */
.site-header{top:0;height:59px;background:var(--white)}
.site-header .brand{left:122px;top:12px;height:34px}
.main-nav{position:absolute;left:383px;top:21px;display:flex;gap:30px;font-size:11.5px;color:#333}
.main-nav .active{color:var(--blue);border-bottom:2px solid var(--blue);padding-bottom:7px}
.phone{position:absolute;left:936px;top:17px;display:flex;align-items:center;gap:8px;font-weight:700;color:var(--navy);font-size:14px}
.phone i{width:24px;height:24px;border-radius:50%;background:var(--gold);display:flex;align-items:center;justify-content:center}

/* hero */
.hero{top:59px;height:560px}
.hero .photo{inset:0;background:linear-gradient(100deg,#7f7463 0%,#b9a074 30%,#e3a93a 48%,#c9b289 62%,#8b8478 100%)}
.hero-frame{position:absolute;left:381px;top:209px;width:432px;height:152px;border:3px solid var(--white);text-align:center;color:var(--white)}
.hero-frame h1{font-size:35px;font-weight:800;line-height:45px;margin-top:12px}
.hero-frame p{font-size:10px;margin-top:2px}
.hero .btn{left:540px;top:349px;width:113px;height:30px}
.hero-curve{position:absolute;left:0;bottom:0}

/* practice band */
.practice{top:617px;height:223px;background:var(--ink)}
.practice .divider{position:absolute;left:599px;top:0;width:2px;height:223px;background:#777}
.practice-item{position:absolute;top:23px;width:420px;text-align:center;color:var(--white)}
.practice-item .icon{width:75px;height:72px;margin:0 auto;display:flex;align-items:center;justify-content:center}
.practice-item h3{font-size:24px;font-weight:700;margin-top:29px}
.practice-item a{display:block;color:var(--gold);font-size:11px;font-weight:700;margin-top:20px}
.practice .brand{left:519px;top:105px;height:33px}

/* experts */
.experts{top:840px;height:520px}
.experts .sec-title{top:52px}
.experts .intro{position:absolute;top:100px;width:1200px;text-align:center;font-size:11.5px;line-height:19px}
.expert{position:absolute;top:185px;width:306px;height:300px}
.expert .photo{left:0;top:0;width:306px;height:270px;border-top:4px solid var(--blue);background:linear-gradient(180deg,#c9ccd0,#7d8185 60%,#3d3f44)}
.expert .plate{position:absolute;left:39px;top:246px;width:216px;height:54px;background:var(--ink);padding:8px 0 0 22px}
.plate h4{color:var(--blue);font-size:11.5px;font-weight:700}
.plate p{color:var(--white);font-size:11px;margin-top:4px}
.plate i{position:absolute;right:16px;top:16px;width:22px;height:22px;border-radius:50%;background:var(--gold)}

/* about */
.about{top:1360px;height:590px;background:linear-gradient(90deg,#cfd0d2 0%,#e9e9ea 45%,#fff 62%)}
.about .photo{left:0;top:0;width:700px;height:590px;background:linear-gradient(120deg,#bfc0c2,#7e7f82 45%,#d6d7d9 80%,rgba(255,255,255,0))}
.about h2{position:absolute;left:610px;top:58px;font-size:25px;font-weight:700;color:var(--navy);display:flex;align-items:center;gap:6px;white-space:nowrap}
.about h2::after{content:"";width:60px;height:2px;background:var(--navy)}
.about p{position:absolute;left:610px;width:460px;font-size:11px;line-height:19px}
.about .btn{left:610px;top:298px;width:114px;height:30px}
.ghost-word{position:absolute;font-weight:800;color:transparent;-webkit-text-stroke:2px rgba(180,180,180,.8);white-space:nowrap}
.about .ghost-word{left:700px;top:388px;font-size:78px;letter-spacing:1px}

/* video */
.video{position:absolute;left:122px;top:1833px;width:955px;height:483px;border:6px solid var(--white);box-shadow:0 4px 18px rgba(0,0,0,.25);background:linear-gradient(135deg,#8b8f96,#3c3f46 50%,#1e2025)}
.video .play{position:absolute;left:432px;top:190px;width:90px;height:90px;border-radius:50%;background:rgba(255,255,255,.75);display:flex;align-items:center;justify-content:center}

/* testimonials */
.testimonials{top:2316px;height:474px;background:linear-gradient(180deg,#fff,#f2f3f5 50%,#fff)}
.testimonials .sec-title{top:70px}
.quote-card{position:absolute;top:164px;width:306px;height:233px;background:var(--white);border-top:4px solid var(--blue);box-shadow:0 2px 10px rgba(0,0,0,.12);text-align:center}
.quote-card .q{position:absolute;left:125px;top:-32px;width:56px;height:56px;border-radius:50%;background:var(--blue);border:4px solid var(--white);color:var(--white);font-size:30px;font-weight:800;line-height:54px}
.quote-card h4{margin-top:50px;font-size:18px;font-weight:700;color:var(--ink)}
.quote-card .role{color:var(--gold);font-size:11px;margin-top:10px}
.quote-card p{font-size:10.5px;line-height:19px;margin:10px 22px 0}
.arrow{position:absolute;top:2586px;width:24px;height:24px;border-radius:50%;border:1.5px solid #333}

/* dual panels */
.dual{top:2790px;height:501px}
.dual .left{position:absolute;left:0;top:0;width:600px;height:501px;background:linear-gradient(160deg,#24305e,#1b2f7a 60%,#27366f)}
.dual .right{position:absolute;left:600px;top:0;width:600px;height:501px;background:linear-gradient(160deg,#4a86c4,#1f64a8 55%,#2d73b4)}
.panel-box{position:absolute;top:154px;width:395px;height:153px;border:3px solid var(--white);color:var(--white);text-align:center}
.panel-box h3{font-size:23px;font-weight:700;margin-top:22px}
.panel-box p{font-size:10.5px;line-height:18px;margin:8px 16px 0}
.panel-box .btn{left:141px;top:136px;width:113px;height:30px}
.dual .brand{left:519px;top:222px;height:33px}

/* blog */
.blog{top:3291px;height:710px}
.blog .sec-title{top:55px}
.post{position:absolute;top:134px;width:468px;height:447px;background:var(--grey-card)}
.post .photo{left:0;top:0;width:468px;height:253px;background:linear-gradient(135deg,#b7b6b3,#5e5b57 55%,#2f2c2a)}
.post .date{position:absolute;left:0;top:0;width:71px;height:66px;background:var(--blue);border:3px solid var(--white);color:var(--white);text-align:center;padding-top:8px}
.date b{display:block;font-size:21px}
.date small{font-size:10px}
.post h3{position:absolute;left:22px;top:285px;font-size:17px;line-height:24px;color:var(--blue-dark);font-weight:600;width:430px;border-left:4px solid var(--blue);padding-left:8px}
.post p{position:absolute;left:34px;top:344px;width:405px;font-size:10.5px;line-height:19px}
.post a{position:absolute;left:34px;top:417px;font-size:10.5px;color:var(--gold);font-weight:600}
.blog .btn{left:536px;top:616px;width:129px;height:30px;z-index:2}
.blog .ghost-word{left:0;width:1200px;text-align:center;top:632px;font-size:62px;-webkit-text-stroke:2px #e2e2e2}

/* call to action */
.cta{top:4001px;height:261px;background:var(--navy)}
.cta .firm{position:absolute;left:24px;top:110px;color:var(--blue);font-weight:800;font-size:20px;width:190px}
.cta .panel{position:absolute;left:240px;top:21px;width:938px;height:221px;background:var(--white);text-align:center}
.cta h2{display:flex;justify-content:center;align-items:center;gap:8px;font-size:33px;font-weight:700;color:var(--navy);margin-top:52px}
.cta h2::before,.cta h2::after{content:"";width:70px;height:2px;background:var(--navy)}
.cta p{font-size:11px;margin-top:10px}
.cta .btn{left:405px;top:147px;width:128px;height:30px}

/* footer */
.site-footer{top:4262px;height:343px;background:var(--ink);color:var(--white)}
.site-footer .brand{left:122px;top:64px;height:38px;background:transparent;border-color:var(--navy)}
.site-footer .brand span{color:var(--blue)}
.about-blurb{position:absolute;left:122px;top:114px;width:260px;font-size:10.5px;line-height:19px}
.social{position:absolute;left:122px;top:204px;display:flex;gap:14px}
.social i{width:26px;height:26px;border-radius:50%;border:1.5px solid var(--white)}
.f-col{position:absolute;top:60px;font-size:10.5px}
.f-col h4{font-size:16px;font-weight:700;margin-bottom:24px}
.f-col li{list-style:none;margin-bottom:15px}
.f-col .gold{color:var(--gold)}
.f-col input{display:block;width:241px;height:33px;background:transparent;border:1px solid #aaa;color:#ccc;font:10px "Montserrat",sans-serif;padding-left:10px;margin-top:14px}
.f-col .btn{position:relative;width:163px;height:30px;margin-top:10px}
.copyright{position:absolute;left:0;top:290px;width:1200px;border-top:1px solid #333;text-align:center;font-size:10px;padding-top:15px}
</style>
</head>
<body>

<header class="site-header">
  <div class="brand"><div class="mark"></div><span>THORNFIELD MARSH, LLC</span></div>
  <nav class="main-nav">
    <span class="active">Home</span><span>About Us ⌄</span><span>Multidistrict Litigation</span><span>Class Actions</span><span>Blog</span><span>Contact</span>
  </nav>
  <div class="phone"><i><svg width="12" height="12" viewBox="0 0 24 24"><path fill="#fff" d="M6.6 10.8a15 15 0 0 0 6.6 6.6l2.2-2.2c.3-.3.7-.4 1-.2 1.1.4 2.3.6 3.6.6.6 0 1 .4 1 1V20c0 .6-.4 1-1 1A17 17 0 0 1 3 4c0-.6.4-1 1-1h3.5c.6 0 1 .4 1 1 0 1.3.2 2.5.6 3.6.1.3 0 .7-.2 1z"/></svg></i>(555) 014 - 2290</div>
</header>

<section class="hero">
  <div class="photo" role="img" aria-label="Classical courthouse columns lit by warm golden sunlight"></div>
  <div class="hero-frame">
    <h1>UNITING CLAIMS,<br>DELIVERING JUSTICE.</h1>
    <p>We are a Multidistrict Litigation &amp; Class Action Expertise</p>
  </div>
  <div class="btn">Learn More <span>⟶</span></div>
  <svg class="hero-curve" width="1200" height="60" viewBox="0 0 1200 60">
    <path d="M0 0 Q600 60 1200 0 L1200 60 L0 60Z" fill="#151515"/>
    <path d="M0 6 Q600 62 1200 6" fill="none" stroke="#3a9fe0" stroke-width="9"/>
  </svg>
</section>

<section class="practice">
  <div class="divider"></div>
  <div class="practice-item" style="left:88px">
    <div class="icon" style="background:var(--navy)"><svg width="40" height="40" viewBox="0 0 40 40" fill="none" stroke="#fff" stroke-width="2"><path d="M20 6v28M10 34h20M8 12h24M8 12l-5 12h10zM32 12l-5 12h10z"/></svg></div>
    <h3>MULTIDISTRICT LITIGATION</h3>
    <a>Learn More</a>
    <svg width="16" height="10" viewBox="0 0 16 10" style="margin-top:6px"><path d="M2 2l6 6 6-6" stroke="#f5a41f" fill="none" stroke-width="1.5"/></svg>
  </div>
  <div class="brand"><div class="mark"></div><span>THORNFIELD MARSH</span></div>
  <div class="practice-item" style="left:693px">
    <div class="icon" style="background:var(--blue)"><svg width="40" height="40" viewBox="0 0 40 40" fill="#fff"><rect x="14" y="6" width="14" height="8" transform="rotate(40 21 10)"/><rect x="19" y="14" width="4" height="16" transform="rotate(-50 21 22)"/><rect x="8" y="31" width="18" height="4"/></svg></div>
    <h3>CLASS ACTIONS PAGE</h3>
    <a>Learn More</a>
    <svg width="16" height="10" viewBox="0 0 16 10" style="margin-top:6px"><path d="M2 2l6 6 6-6" stroke="#f5a41f" fill="none" stroke-width="1.5"/></svg>
  </div>
</section>

<section class="experts">
  <h2 class="sec-title">MEET OUR EXPERTS</h2>
  <p class="intro">Lorem ipsum dolor sit amet, consectetur adipiscing elit.<br>Nullam venenatis tempus est, eu pulvinar erat porttitor in.</p>
  <article class="expert" style="left:122px">
    <div class="photo" role="img" aria-label="Portrait of attorney Leonard Thornfield in an office"></div>
    <div class="plate"><h4>LEONARD THORNFIELD</h4><p>Attorney</p><i></i></div>
  </article>
  <article class="expert" style="left:447px">
    <div class="photo" role="img" aria-label="Portrait of attorney Brent Marsh seated at a desk with a laptop"></div>
    <div class="plate"><h4>BRENT MARSH</h4><p>Attorney</p><i></i></div>
  </article>
  <article class="expert" style="left:772px">
    <div class="photo" role="img" aria-label="Portrait of legal assistant Melinda Carrow in the office"></div>
    <div class="plate"><h4>MELINDA CARROW</h4><p>Legal Assistant</p><i></i></div>
  </article>
</section>

<section class="about">
  <div class="photo" role="img" aria-label="Greyscale view of a classical courthouse facade with engraved frieze"></div>
  <div class="ghost-word">ABOUT US</div>
  <h2>ABOUT THORNFIELD MARSH, LLC</h2>
  <p style="top:100px">Lorem ipsum dolor sit amet, consectetur adipiscing elit. Nullam venenatis tempus est, eu pulvinar erat porttitor in. Donec lobortis tortor quis tortor mattis, eu sagittis nulla ultrices. Quisque egestas nibh purus, sit amet vehicula est ullamcorper ut. In ac posuere nisl. Fusce elementum ligula non consequat iaculis.</p>
  <p style="top:194px">Lorem ipsum dolor sit amet, consectetur adipiscing elit. Nullam venenatis tempus est, eu pulvinar erat porttitor in. Donec lobortis tortor quis tortor mattis, eu sagittis nulla ultrices. Quisque egestas nibh purus, sit amet vehicula est ullamcorper ut. In ac posuere nisl. Fusce elementum ligula non consequat iaculis.</p>
  <div class="btn">Learn More <span>⟶</span></div>
</section>

<div class="video" role="img" aria-label="Video still of a lawyer signing documents beside scales of justice and a gavel">
  <div class="play"><svg width="26" height="28" viewBox="0 0 26 28"><path d="M4 2l20 12L4 26z" fill="#3a9fe0"/></svg></div>
</div>

<section class="testimonials">
  <h2 class="sec-title">CLIENT TESTIMONIALS</h2>
  <article class="quote-card" style="left:122px"><div class="q">“</div><h4>Renata Oakes</h4><div class="role">Businessman</div><p>“Lorem ipsum dolor sit amet, consectetur adipiscing elit. Donec condimentum leo sed cursus iaculis. Quisque eu dapibus odio. Donec scelerisque maximus sodal Praesent eget iaculis libero, non pulvinareros.”</p></article>
  <article class="quote-card" style="left:447px"><div class="q">“</div><h4>Dominic Harlowe</h4><div class="role">Businessman</div><p>“Lorem ipsum dolor sit amet, consectetur adipiscing elit. Donec condimentum leo sed cursus iaculis. Quisque eu dapibus odio. Donec scelerisque maximus sodal Praesent eget iaculis libero, non pulvinareros.”</p></article>
  <article class="quote-card" style="left:772px"><div class="q">“</div><h4>Wesley Brandt</h4><div class="role">Businessman</div><p>“Lorem ipsum dolor sit amet, consectetur adipiscing elit. Donec condimentum leo sed cursus iaculis. Quisque eu dapibus odio. Donec scelerisque maximus sodal Praesent eget iaculis libero, non pulvinareros.”</p></article>
</section>
<svg class="arrow" style="left:79px" viewBox="0 0 24 24"><path d="M14 7l-5 5 5 5" stroke="#333" fill="none" stroke-width="1.5"/></svg>
<svg class="arrow" style="left:1096px" viewBox="0 0 24 24"><path d="M10 7l5 5-5 5" stroke="#333" fill="none" stroke-width="1.5"/></svg>

<section class="dual">
  <div class="left" role="img" aria-label="Navy-toned photo of a lawyer with a miniature house model"></div>
  <div class="right" role="img" aria-label="Blue-toned photo of a judge's gavel and documents"></div>
  <div class="panel-box" style="left:102px">
    <h3>MULTIDISTRICT LITIGATION</h3>
    <p>Lorem ipsum dolor sit amet, consectetur adipiscing elit. Nullam venenatis tempus est, eu pulvinar erat porttitor in. Donec lobortis tortor quis tortor mattis, eu sagittis nulla ultrices.</p>
    <div class="btn">Learn More <span>⟶</span></div>
  </div>
  <div class="brand"><div class="mark"></div><span>THORNFIELD MARSH</span></div>
  <div class="panel-box" style="left:701px">
    <h3>CLASS ACTIONS</h3>
    <p>Lorem ipsum dolor sit amet, consectetur adipiscing elit. Nullam venenatis tempus est, eu pulvinar erat porttitor in. Donec lobortis tortor quis tortor mattis, eu sagittis nulla ultrices.</p>
    <div class="btn">Learn More <span>⟶</span></div>
  </div>
</section>

<section class="blog">
  <h2 class="sec-title">BLOG &amp; NEWS</h2>
  <article class="post" style="left:122px">
    <div class="photo" role="img" aria-label="Lawyer at a desk with a gavel and an open book"></div>
    <div class="date"><b>29</b><small>March</small></div>
    <h3>Lorem ipsum dolor sit amet, consectetur<br>adipiscing elit Donec condimentum</h3>
    <p>Lorem ipsum dolor sit amet, consectetur adipiscing elit. Donec condimentum leo sed cursus iaculis. Quisque eu dapibus odio. Donec scelerisque maximus sodales Praesent eget iaculis libero.</p>
    <a>Learn More ⟶</a>
  </article>
  <article class="post" style="left:610px">
    <div class="photo" role="img" aria-label="Lawyer reviewing papers beside brass scales of justice"></div>
    <div class="date"><b>29</b><small>March</small></div>
    <h3>Lorem ipsum dolor sit amet, consectetur<br>adipiscing elit Donec condimentum</h3>
    <p>Lorem ipsum dolor sit amet, consectetur adipiscing elit. Donec condimentum leo sed cursus iaculis. Quisque eu dapibus odio. Donec scelerisque maximus sodales Praesent eget iaculis libero.</p>
    <a>Learn More ⟶</a>
  </article>
  <div class="ghost-word">THORNFIELD MARSH, LLC</div>
  <div class="btn">View All Blog <span>⟶</span></div>
</section>

<section class="cta">
  <div class="firm">THORNFIELD MARSH, LLC</div>
  <div class="panel">
    <h2>JOIN THE FIGHT—START YOUR CLAIM</h2>
    <p>We're Here to Help—Get a Free Case Review</p>
    <div class="btn">Get Started</div>
  </div>
</section>

<footer class="site-footer">
  <div class="brand"><div class="mark"></div><span>THORNFIELD MARSH, LLC</span></div>
  <p class="about-blurb">Lorem ipsum dolor sit amet, consectetur adipiscing elit. Donec condimentum leo sed cursus iaculis. Quisque eu dapibus odio. Donec scelerisque maximus sodales.</p>
  <div class="social"><i></i><i></i><i></i><i></i></div>
  <div class="f-col" style="left:427px">
    <h4>NAVIGATION</h4>
    <ul><li>Home</li><li>About Us</li><li>Multidistrict Litigation</li><li>Class Actions</li><li>Blog</li><li>Contact</li></ul>
  </div>
  <div class="f-col" style="left:624px">
    <h4>CONTACT US</h4>
    <ul><li>Suite 12, 88 Harbor Lane<br>Riverton 40210</li><li>555 014 2291</li><li class="gold">contact@thornfieldmarsh.example</li></ul>
  </div>
  <div class="f-col" style="left:837px">
    <h4>SUBSCRIBE NEWSLETTER</h4>
    <div>Subscribe to our newsletter</div>
    <input type="text" placeholder="Enter your email">
    <div class="btn">Subscribe</div>
  </div>
  <div class="copyright">© Copyright Thornfield Marsh, LLC. All Rights Reserved</div>
</footer>

</body>
</html>
```